Private Maths Tuition Flyer based in London

I am opening up a new Maths tuition centre in North West London. The flyer will be delivered to over 8,000 homes within the immediate vicinity. The design should be suitable to be printed on an A5 sheet and read in a portrait orientation.

The flyer should include the following:

The headline statement should be "Private Maths Tuition"

Secondary headline statement is the following "GCSE, A-Levels, 11 Plus exams"

Some of service offerings/selling points are:

- Free first session
- Monthly Feedback reports
- Free support outside of sessions
- Clear Target grades
- Personalised Lesson plans
- Tangible Results

Another statement that should be featured is "Book your free session by visiting www.lernova.co.uk" or something similar to that.

"Contact Details:
020 4719 8263
enquiries@lernova.co.uk"

"Address:
Kelbridge Business and Innovation Centre
Ashvale Court
Wrenfield Road
HA4 9QD"

Attached you'll see a logo which should be included and also a map of where we are. I am open to new images for the map if you guys have any, rather than a screen shot from google maps but it should be clear to see.

I would like the content above to be displayed in a clear and concise manner that is easy to read. You have creative license on where this information should be displayed and where the images should be but on the whole it should look aesthetically pleasing on the eye.

Target Market(s)

Students, Parents. Parents who want maths tutors.

Industry/Entity Type

Tutoring

Font styles to use
Sans Serif

Requirements
Must have
• *logo*
• Private Maths Tuition
• GCSE, A-Levels, 11 Plus exams
• - Free first session
• - Monthly Feedback reports
• - Free support outside of sessions
• - Clear Target grades
• - Personalised Lesson plans
• - Tangible Results
• Book your free session by visiting www.lernova.co.uk" or something similar to that.
• Contact Details:
• 020 4719 8263
• enquiries@lernova.co.uk
• Address (*with map*):
• Kelbridge Business and Innovation Centre
• Ashvale Court
• Wrenfield Road
• HA4 9QD
Nice to have
• similar colour scheme as the logo. creative background design.

```html
<!DOCTYPE html>
<html lang="en">
<head>
<meta charset="utf-8">
<title>Lernova – Private Maths Tuition</title>
<link rel="stylesheet" href="https://fonts.googleapis.com/css2?family=Montserrat:wght@700;800&family=Oswald:wght@500;600&family=Roboto+Condensed:wght@400;500&family=Open+Sans:wght@400;600&display=swap">
<style>
  :root{
    --orange:#f26a21;
    --orange-light:#f7941d;
    --blue:#1d4f91;
    --blue-dark:#173e78;
    --green:#8cc63f;
    --green-dark:#6fae2a;
    --text:#444a50;
    --white:#ffffff;
  }
  *{box-sizing:border-box;margin:0;padding:0}
  html,body{width:999px;height:1200px;overflow:hidden;background:var(--white)}
  .flyer{position:relative;width:999px;height:1200px;background:linear-gradient(#f4f5f6,#e9ebec);overflow:hidden;font-family:"Open Sans",Arial,sans-serif}
  .top-rule{position:absolute;top:0;left:0;right:0;height:9px;display:flex}
  .top-rule span:first-child{flex:0 0 48%;background:var(--green)}
  .top-rule span:last-child{flex:1;background:var(--blue)}
  .hero-still{position:absolute;top:9px;left:0;width:640px;height:360px;background:linear-gradient(135deg,#d9dcdf 0%,#eceeef 55%,#f5f6f7 100%)}
  .hero-portrait{position:absolute;top:22px;left:660px;width:325px;height:350px;background:linear-gradient(160deg,#cfd6dc 0%,#e6e2da 45%,#c9a97a 75%,#e9ebee 100%)}
  .brand{position:absolute;top:258px;left:290px;display:flex;align-items:center;gap:16px}
  .brand-dot{width:34px;height:34px;border-radius:50%;background:var(--green)}
  .brand-name{font-family:"Montserrat",Arial,sans-serif;font-weight:700;font-size:68px;line-height:1;color:var(--orange);letter-spacing:-1px;white-space:nowrap}
  .headline{position:absolute;top:378px;left:0;right:0;height:78px;background:linear-gradient(90deg,var(--orange),var(--orange-light) 50%,var(--orange));display:flex;align-items:center;justify-content:center;font-family:"Montserrat",Arial,sans-serif;font-weight:800;font-size:48px;color:var(--white);letter-spacing:.5px;white-space:nowrap}
  .subhead{position:absolute;top:474px;left:220px;width:560px;height:62px;background:var(--blue);display:flex;align-items:center;justify-content:center;font-family:"Oswald",Arial,sans-serif;font-weight:500;font-size:34px;line-height:1;color:var(--white);white-space:nowrap}
  .offer{position:absolute;top:568px;left:95px;width:850px;height:182px;background:var(--white);border:3px solid var(--green);border-radius:18px}
  .offer-tab{position:absolute;top:-20px;left:228px;width:365px;height:46px;background:var(--green);border-radius:0 0 16px 16px;display:flex;align-items:center;justify-content:center;font-family:"Montserrat",Arial,sans-serif;font-weight:700;font-size:25px;color:var(--white);white-space:nowrap}
  .offer-list{position:absolute;top:50px;left:68px;right:30px;display:grid;grid-template-columns:428px 1fr;grid-auto-flow:column;grid-template-rows:repeat(3,38px);list-style:none}
  .offer-list li{display:flex;align-items:center;gap:12px;font-size:20px;color:var(--text);white-space:nowrap}
  .tick{width:22px;height:22px;flex:none}
  .cta{position:absolute;top:775px;left:292px;width:415px;height:66px;border-radius:24px;background:linear-gradient(var(--orange-light),var(--orange));display:flex;align-items:center;justify-content:center;font-family:"Oswald",Arial,sans-serif;font-weight:500;font-size:34px;line-height:1;color:var(--white);white-space:nowrap}
  .cta-url{position:absolute;top:847px;left:372px;width:255px;height:50px;border-radius:22px;background:var(--blue);display:flex;align-items:center;justify-content:center;font-family:"Oswald",Arial,sans-serif;font-weight:500;font-size:26px;line-height:1;color:var(--white);white-space:nowrap}
  .footer-panel{position:absolute;top:905px;left:120px;width:856px;height:225px;background:linear-gradient(160deg,var(--green),var(--green-dark));border-radius:40px 40px 0 0}
  .contact{position:absolute;top:36px;left:42px;list-style:none;font-family:"Roboto Condensed",Arial,sans-serif;font-size:18px;color:var(--white);line-height:21px}
  .contact li{display:flex;gap:9px;margin-bottom:8px;white-space:nowrap}
  .contact svg{width:17px;height:17px;flex:none;margin-top:2px}
  .social{display:flex;gap:7px;margin-top:4px}
  .social span{width:26px;height:26px;border-radius:50%;border:2px solid var(--white)}
  .map{position:absolute;top:28px;left:445px;width:390px;height:165px;border:5px solid var(--white);border-radius:10px;background:linear-gradient(135deg,#e3e3df,#d5dccb 60%,#e8e6e1)}
  .base-band{position:absolute;left:0;right:0;top:1130px;height:70px;background:var(--blue-dark)}
  .base-band::before{content:"";position:absolute;top:-14px;left:120px;width:856px;height:14px;background:var(--blue)}
</style>
</head>
<body>
<main class="flyer">
  <div class="top-rule"><span></span><span></span></div>
  <div class="hero-still" role="img" aria-label="Soft grey photograph of reading glasses on a desk"></div>
  <div class="hero-portrait" role="img" aria-label="Photograph of a smiling young tutor with arms folded"></div>

  <div class="brand">
    <span class="brand-dot"></span>
    <span class="brand-name">Lernova</span>
  </div>

  <h1 class="headline">PRIVATE MATHS TUITION</h1>
  <h2 class="subhead">GCSE, A-Levels, 11 Plus exams</h2>

  <section class="offer">
    <div class="offer-tab">What we offer</div>
    <ul class="offer-list">
      <li><svg class="tick" viewBox="0 0 20 20"><rect x="1.5" y="3.5" width="14" height="14" fill="none" stroke="#f26a21" stroke-width="2"/><path d="M5 10l4 4 9-11" fill="none" stroke="#f26a21" stroke-width="2.6"/></svg>Free first session</li>
      <li><svg class="tick" viewBox="0 0 20 20"><rect x="1.5" y="3.5" width="14" height="14" fill="none" stroke="#f26a21" stroke-width="2"/><path d="M5 10l4 4 9-11" fill="none" stroke="#f26a21" stroke-width="2.6"/></svg>Monthly Feedback reports</li>
      <li><svg class="tick" viewBox="0 0 20 20"><rect x="1.5" y="3.5" width="14" height="14" fill="none" stroke="#f26a21" stroke-width="2"/><path d="M5 10l4 4 9-11" fill="none" stroke="#f26a21" stroke-width="2.6"/></svg>Free support outside of sessions</li>
      <li><svg class="tick" viewBox="0 0 20 20"><rect x="1.5" y="3.5" width="14" height="14" fill="none" stroke="#f26a21" stroke-width="2"/><path d="M5 10l4 4 9-11" fill="none" stroke="#f26a21" stroke-width="2.6"/></svg>Clear Target grades</li>
      <li><svg class="tick" viewBox="0 0 20 20"><rect x="1.5" y="3.5" width="14" height="14" fill="none" stroke="#f26a21" stroke-width="2"/><path d="M5 10l4 4 9-11" fill="none" stroke="#f26a21" stroke-width="2.6"/></svg>Personalised Lesson plans</li>
      <li><svg class="tick" viewBox="0 0 20 20"><rect x="1.5" y="3.5" width="14" height="14" fill="none" stroke="#f26a21" stroke-width="2"/><path d="M5 10l4 4 9-11" fill="none" stroke="#f26a21" stroke-width="2.6"/></svg>Tangible Results</li>
    </ul>
  </section>

  <div class="cta">BOOK YOUR FREE SESSION</div>
  <div class="cta-url">www.lernova.co.uk</div>

  <section class="footer-panel">
    <ul class="contact">
      <li><svg viewBox="0 0 16 16"><path d="M8 1a5 5 0 0 0-5 5c0 4 5 9 5 9s5-5 5-9a5 5 0 0 0-5-5z" fill="#f26a21"/><circle cx="8" cy="6" r="2" fill="#fff"/></svg><span>Kelbridge Business and Innovation Centre,<br>Ashvale Court, Wrenfield Road, HA4 9QD</span></li>
      <li><svg viewBox="0 0 16 16"><rect x="1" y="3" width="14" height="10" fill="#f26a21"/><path d="M1 3l7 6 7-6" fill="none" stroke="#fff" stroke-width="1.5"/></svg><span>enquiries@lernova.co.uk</span></li>
      <li><svg viewBox="0 0 16 16"><circle cx="8" cy="8" r="7" fill="#f26a21"/><path d="M1 8h14M8 1c-3 4-3 10 0 14M8 1c3 4 3 10 0 14" fill="none" stroke="#fff" stroke-width="1"/></svg><span>www.lernova.co.uk</span></li>
      <li><svg viewBox="0 0 16 16"><rect x="1" y="1" width="14" height="14" rx="3" fill="#f26a21"/><path d="M5 4l2 2-1 1.5c.8 1.5 1.5 2.2 3 3L10.5 9l2 2-1.5 1.5C7.5 12 4 8.5 3.5 5z" fill="#fff"/></svg><span>020 4719 8263</span></li>
      <li class="social"><span></span><span></span><span></span><span></span></li>
    </ul>
    <div class="map" role="img" aria-label="Street map showing the location of Kelbridge Business and Innovation Centre, Ashvale Court, Wrenfield Road, HA4 9QD"></div>
  </section>

  <div class="base-band"></div>
</main>
</body>
</html>
```